Business Card Design

I need a business card for my rental business. The business is named:
Cruise a Trikeway Houston
www.cruiseatrikewayhouston.com
(832) 555-0193
This will be a business card that I will leave at other businesses as advertisement so it needs to have the name, website, and phone number.
Please feel free to be creative. This is a new business so I have no designs.
Thank you very much for your time and I look forward to receiving your designs
Target Market(s)
Local rental customers
Industry/Entity Type
Business
Contact Information for Business Card
Please check out my website:
Font styles to use
Other font styles liked:
- anything creative
Colors
Designer to choose colors to be used in the design.
Requirements
Must have
- Business name, phone, website. Rentals available hourly or daily. Book online

```html
<!DOCTYPE html>
<html lang="en">
<head>
<meta charset="utf-8">
<title>Cruise a Trikeway Houston – Business Card</title>
<link href="https://fonts.googleapis.com/css2?family=Didact+Gothic&family=Quicksand:wght@500;600&display=swap" rel="stylesheet">
<style>
  :root {
    --pink: #e8375a;
    --ink: #2b2b30;
    --card-light: #e1e4e7;
    --card-lighter: #e9ebeb;
    --panel-grey: #d1d6d9;
    --dark-start: #05070b;
    --dark-end: #333437;
    --white: #ffffff;
  }
  * { margin: 0; padding: 0; box-sizing: border-box; }
  html, body {
    width: 1200px; height: 1200px; overflow: hidden; background: var(--white);
  }
  .canvas { position: relative; width: 1200px; height: 1200px; }
  .card {
    position: absolute; left: 179px; width: 1051px; height: 600px;
    transform: scale(0.8); transform-origin: 0 0; overflow: hidden;
  }
  .card--front { top: 59px; }
  .card--back { top: 606px; }
  .card__shapes { position: absolute; inset: 0; width: 1051px; height: 600px; }
  .text {
    position: absolute; white-space: nowrap; color: var(--ink);
    font-family: "Didact Gothic", sans-serif;
  }
  .front-name { left: 260px; top: 347px; transform: translate(-50%, -50%);
    color: var(--white); font-family: "Quicksand", sans-serif; font-weight: 500; font-size: 27px; letter-spacing: 0.5px; }
  .front-heading { left: 586px; top: 128px; transform: translateY(-50%); font-size: 30px; }
  .contact-phone { left: 586px; top: 278px; transform: translateY(-50%); font-size: 31px; letter-spacing: 1px; }
  .contact-web { left: 586px; top: 359px; transform: translateY(-50%); font-size: 27px; }
  .contact-address { left: 586px; top: 420px; font-size: 30px; line-height: 40px; }
  .back-name { left: 531px; top: 377px; transform: translate(-50%, -50%);
    font-family: "Quicksand", sans-serif; font-weight: 600; font-size: 46px; letter-spacing: 1px; }
  .back-tagline { left: 525px; top: 494px; transform: translate(-50%, -50%);
    color: var(--white); font-family: "Quicksand", sans-serif; font-weight: 500; font-size: 33px; }
</style>
</head>
<body>
<main class="canvas">

  <section class="card card--front" aria-label="Business card front">
    <svg class="card__shapes" viewBox="0 0 1051 600" aria-hidden="true">
      <defs>
        <linearGradient id="darkPanel" x1="0" x2="1" y1="0" y2="0">
          <stop offset="0" stop-color="var(--dark-start)"/>
          <stop offset="1" stop-color="var(--dark-end)"/>
        </linearGradient>
      </defs>
      <rect width="1051" height="600" fill="var(--card-light)"/>
      <polygon points="386,0 661,0 524,69" fill="var(--panel-grey)"/>
      <polygon points="386,600 661,600 524,530" fill="var(--panel-grey)"/>
      <polygon points="0,0 386,0 524,69 524,530 386,600 0,600" fill="url(#darkPanel)"/>
      <polygon points="473,101 524,69 577,101 577,161 524,191 473,161" fill="var(--pink)"/>
      <polygon points="473,222 524,191 577,222 577,498 524,530 473,498" fill="var(--pink)"/>
      <!-- phone icon -->
      <path d="M510 232 q-6 3 -4 14 q6 24 26 40 q8 5 13 0 l4 -5 -12 -10 -6 5 q-10 -7 -14 -20 l6 -4 -6 -14 z" fill="none" stroke="var(--white)" stroke-width="4" stroke-linejoin="round"/>
      <!-- globe icon -->
      <g fill="none" stroke="var(--white)" stroke-width="4">
        <circle cx="524" cy="360" r="28"/>
        <ellipse cx="524" cy="360" rx="12" ry="28"/>
        <line x1="496" y1="360" x2="552" y2="360"/>
      </g>
      <!-- home icon -->
      <g fill="var(--white)">
        <polygon points="524,430 556,458 550,464 524,441 498,464 492,458"/>
        <polygon points="503,464 524,446 545,464 545,489 530,489 530,474 518,474 518,489 503,489"/>
      </g>
    </svg>
    <p class="text front-name">Cruise a Trikeway Houston</p>
    <p class="text front-heading">Cruise a Trikeway Houston</p>
    <p class="text contact-phone">(832) 555-0193</p>
    <p class="text contact-web">www.cruiseatrikewayhouston.com</p>
    <p class="text contact-address">1200 Harbor Loop, Houston,<br>Texas 77099, United States</p>
  </section>

  <section class="card card--back" aria-label="Business card back">
    <svg class="card__shapes" viewBox="0 0 1051 600" aria-hidden="true">
      <rect width="1051" height="600" fill="var(--card-lighter)"/>
      <polygon points="96,0 955,0 748,600 289,600" fill="var(--panel-grey)"/>
      <rect x="0" y="491" width="1051" height="6" fill="var(--pink)"/>
      <polygon points="136,494 164,442 886,442 914,494 886,546 164,546" fill="var(--pink)"/>
    </svg>
    <p class="text back-name">Cruise a Trikeway Houston</p>
    <p class="text back-tagline">Rentals available hourly or daily. Book online</p>
  </section>

</main>
</body>
</html>
```